Italian Dinning Table and wardrobe Selling Website

We need a website design for a reputable furniture company deals in the manufacture of Italian dinning tables and wardrobe. We provide our services to USA based customers.

The categories of the website are
- Home page
- Product page
- The page where all the items are sold
- The shopping cart page

The website is required to have several areas of products with prices that can be added to shopping cart.
Also the website should have customer login facility along with privacy policy, contact us, about us and terms of use
Preferred colors are brown, black and pink,

It Company

```html
<!DOCTYPE html>
<html lang="en">
<head>
<meta charset="utf-8">
<title>Verona Home Furnishings</title>
<link href="https://fonts.googleapis.com/css2?family=Cinzel:wght@400;600&family=Lato:wght@400;700&display=swap" rel="stylesheet">
<style>
:root{
  --beige:#d6c5ab;
  --brown:#5a3a1e;
  --brown-dark:#3e2914;
  --page:#f1f1f1;
  --white:#ffffff;
  --ink:#2b2b2b;
  --muted:#555555;
  --line:#dcdcdc;
  --black:#0d0d0d;
  --footer-bar:#4a2f17;
}
*{margin:0;padding:0;box-sizing:border-box}
html,body{width:1200px;height:3093px;overflow:hidden}
body{position:relative;background:var(--page);font-family:'Lato',Arial,sans-serif;color:var(--ink)}
.abs{position:absolute}
a{color:inherit;text-decoration:none}

/* header */
.header-band{left:0;top:0;width:1200px;height:660px;background:var(--beige)}
.brand{left:161px;top:22px;display:flex;align-items:center;gap:14px}
.brand-dot{width:52px;height:52px;border-radius:50%;background:var(--brown)}
.brand-name{font-family:'Cinzel',Georgia,serif;font-weight:600;font-size:26px;line-height:1.05;color:var(--brown)}
.top-links{right:161px;top:8px;display:flex;gap:22px;font-size:11px;color:var(--ink);align-items:center}
.top-links span{display:flex;align-items:center;gap:6px}
.contact-row{right:161px;top:62px;display:flex;gap:26px;font-size:14px;font-weight:700;color:var(--ink)}
.contact-row span{display:flex;align-items:center;gap:8px}
.nav{left:161px;top:113px;width:878px;height:36px;border-top:1px solid #a89478;border-bottom:1px solid #a89478;display:flex;justify-content:space-between;align-items:center;font-size:12px;letter-spacing:.5px;text-transform:uppercase;color:var(--white)}
.nav .active{color:var(--brown-dark);font-weight:700;border-bottom:2px solid var(--brown-dark);padding-bottom:4px}
.hero-kicker{left:161px;top:322px;font-family:'Cinzel',Georgia,serif;font-size:27px;letter-spacing:2px;color:var(--white)}
.hero-title{left:161px;top:360px;font-family:'Cinzel',Georgia,serif;font-weight:600;font-size:25px;line-height:1.35;letter-spacing:1px;color:var(--brown-dark)}
.hero-photo{left:598px;top:170px;width:526px;height:428px;border-radius:40% 40% 8px 8px;background:radial-gradient(ellipse at 50% 40%,#e6d2ac,#b9a17a 70%,rgba(214,197,171,0) 72%)}
.slide-arrow{top:372px}

/* category */
.cat-card{left:161px;top:614px;width:878px;height:349px;background:var(--white);box-shadow:0 2px 6px rgba(0,0,0,.08)}
.cat{top:33px;width:385px;height:285px;display:flex;flex-direction:column;align-items:center;justify-content:center;color:var(--white);text-align:center}
.cat-1{left:35px;background:linear-gradient(135deg,#3b3430,#1c1816 60%,#4a3d30)}
.cat-2{left:458px;background:linear-gradient(135deg,#5b5650,#262320 55%,#6b655c)}
.cat h3{font-family:'Cinzel',Georgia,serif;font-weight:400;font-size:25px;letter-spacing:1px;margin-top:40px}
.cat p{font-size:15px;margin-top:6px}
.cat .cta{font-size:14px;font-weight:700;margin-top:4px;text-transform:uppercase}

/* section headings */
.section-title{left:0;width:1200px;text-align:center;font-family:'Cinzel',Georgia,serif;font-size:24px;letter-spacing:1.5px}
.section-title::after{content:"";display:block;width:80px;height:1px;background:#bbb;margin:12px auto 0}
.featured-title{top:1068px;color:var(--brown)}

/* products */
.product{top:1140px;width:206px;height:258px;background:var(--white);border:1px solid var(--line);text-align:center}
.product .ph{width:150px;height:140px;margin:18px auto 0}
.product h4{font-size:13px;font-weight:400;margin-top:18px}
.product .btn{display:inline-block;margin-top:18px;width:114px;height:30px;line-height:28px;border:1px solid var(--line);font-size:11px;color:#b9b9b9;text-transform:uppercase}
.product .btn.on{color:var(--ink);border-color:#999}
.carousel-arrow{top:1250px;width:30px;height:38px;background:var(--white);border:1px solid var(--line);display:flex;align-items:center;justify-content:center}

/* news */
.news-band{left:0;top:1460px;width:1200px;height:256px;background:linear-gradient(90deg,#1b1612,#2e2620 50%,#1b1612)}
.news-title{top:1538px;color:var(--white)}
.news{top:1619px;width:278px;height:371px;background:var(--white);border:1px solid var(--line)}
.news .ph{position:absolute;left:12px;top:14px;width:254px;height:168px}
.news .date{position:absolute;left:12px;top:0;width:44px;text-align:center;color:var(--white);font-size:15px;font-weight:700}
.news .date b{display:block;background:var(--brown);height:26px;line-height:26px}
.news .date i{display:block;background:#2a2a2a;font-style:normal;font-size:11px;height:22px;line-height:22px}
.news h4{position:absolute;left:12px;top:196px;width:254px;font-size:13px;line-height:1.45;font-weight:700}
.news p{position:absolute;left:12px;top:260px;width:254px;font-size:12px;line-height:1.45;color:var(--muted)}
.news .more{position:absolute;left:12px;top:340px;font-size:12px;font-weight:700;display:flex;align-items:center;gap:6px}

/* features */
.feature{top:2050px;width:260px;text-align:center}
.feature .circle{width:113px;height:113px;border-radius:50%;margin:0 auto;display:flex;align-items:center;justify-content:center}
.feature h5{margin-top:22px;font-size:14px;font-weight:700;text-transform:uppercase;white-space:nowrap}
.feature p{margin:6px auto 0;width:240px;font-size:12px;line-height:1.45;color:var(--muted)}

/* newsletter */
.newsletter{left:161px;top:2326px;width:878px;height:351px;background:var(--white)}
.newsletter .ph{position:absolute;left:35px;top:30px;width:385px;height:290px;background:radial-gradient(ellipse at 45% 45%,#4a4a4a,#1a1a1a 45%,rgba(255,255,255,0) 62%)}
.newsletter h3{position:absolute;left:420px;width:420px;top:122px;text-align:center;font-family:'Cinzel',Georgia,serif;font-weight:400;font-size:24px;letter-spacing:1.5px;color:var(--brown-dark)}
.newsletter p{position:absolute;left:420px;width:420px;top:176px;text-align:center;font-size:12px;line-height:1.5;color:var(--ink)}
.newsletter .field{position:absolute;left:431px;top:241px;width:300px;height:32px;border:1px solid var(--line);font-size:10px;color:#999;padding:9px 10px}
.newsletter .submit{position:absolute;left:742px;top:241px;width:103px;height:32px;background:var(--brown-dark);color:var(--white);font-size:13px;font-weight:700;text-align:center;line-height:32px}

/* footer */
.footer{left:0;top:2753px;width:1200px;height:295px;background:linear-gradient(90deg,#050505,#161513 55%,#0a0a0a)}
.footer-brand{left:0;top:2790px;width:1200px;display:flex;justify-content:center;align-items:center;gap:10px}
.footer-brand .dot{width:36px;height:36px;border-radius:50%;background:#8a7558}
.footer-brand span{font-family:'Cinzel',Georgia,serif;font-weight:600;font-size:17px;color:#c9b594;line-height:1.1}
.footer-nav{left:0;top:2864px;width:1200px;display:flex;justify-content:center;gap:42px;font-size:12px;color:var(--white);font-weight:700}
.footer-contact{top:2930px;display:flex;align-items:center;gap:14px;color:var(--white);font-size:12px;line-height:1.4;white-space:nowrap}
.footer-contact .ring{width:50px;height:50px;border-radius:50%;border:1px solid #888;display:flex;align-items:center;justify-content:center;flex:none}
.footer-links{left:0;top:3018px;width:1200px;text-align:center;font-size:11px;color:var(--white)}
.footer-links span{margin:0 10px}
.footer-bar{left:0;top:3048px;width:1200px;height:45px;background:var(--footer-bar)}
.copyright{left:161px;top:3064px;font-size:10px;font-weight:700;color:var(--white)}
.socials{right:161px;top:3058px;display:flex;gap:6px}
.socials i{width:24px;height:24px;border-radius:50%;background:#2f6fb5;display:block}
</style>
</head>
<body>

<div class="abs header-band"></div>
<div class="abs brand"><div class="brand-dot"></div><div class="brand-name">VERONA<br>HOME FURNISHINGS</div></div>
<div class="abs top-links">
  <span><svg width="11" height="11" viewBox="0 0 12 12"><circle cx="5" cy="5" r="3.5" fill="none" stroke="#2b2b2b" stroke-width="1.5"/><line x1="7.5" y1="7.5" x2="11" y2="11" stroke="#2b2b2b" stroke-width="1.5"/></svg></span>
  <span>Sign In</span><span>My Account</span><span>Check Out</span>
  <span><svg width="26" height="24" viewBox="0 0 26 24"><path d="M2 4h4l3 11h12l3-8H8" fill="none" stroke="#2b2b2b" stroke-width="1.6"/><circle cx="11" cy="19" r="2" fill="#2b2b2b"/><circle cx="19" cy="19" r="2" fill="#2b2b2b"/></svg></span>
</div>
<div class="abs contact-row">
  <span><svg width="14" height="14" viewBox="0 0 14 14"><path d="M3 1l2.5 3-1.5 1.5c1 2 2.5 3.5 4.5 4.5L10 8.5 13 11l-1.5 2C6 13 1 8 1 2.5z" fill="#2b2b2b"/></svg>555-018-2040</span>
  <span><svg width="14" height="14" viewBox="0 0 14 14"><path d="M1 6l12-5-5 12-2-5z" fill="#2b2b2b"/></svg>hello@veronahome.example</span>
</div>
<nav class="abs nav">
  <a class="active">Home</a><a>Italian Dining Tables</a><a>Wooden Wardrobes</a><a>Product Category</a><a>About</a><a>FAQ's</a><a>Contact</a>
</nav>
<div class="abs hero-kicker">WE DO MANUFACTURING OF</div>
<div class="abs hero-title">ITALIAN DINING TABLES &amp;<br>WOODEN WARDROBES IN USA</div>
<div class="abs hero-photo" role="img" aria-label="Cream lacquered Italian dining table with upholstered chairs and a vase of red roses"></div>
<svg class="abs slide-arrow" style="left:20px" width="44" height="20" viewBox="0 0 44 20"><path d="M42 10H3M10 3L3 10l7 7" fill="none" stroke="#2b2b2b" stroke-width="1.5"/></svg>
<svg class="abs slide-arrow" style="left:1136px" width="44" height="20" viewBox="0 0 44 20"><path d="M2 10h39M34 3l7 7-7 7" fill="none" stroke="#2b2b2b" stroke-width="1.5"/></svg>

<section class="abs cat-card">
  <div class="abs cat cat-1" role="img" aria-label="Dark Italian dining room with glass cabinet and chandelier">
    <h3>ITALIAN DINING TABLES</h3><p>Good design is always in season</p><span class="cta">Shop Now &rarr;</span>
  </div>
  <div class="abs cat cat-2" role="img" aria-label="Bedroom with tall dark sliding wardrobe">
    <h3>WOODEN WARDROBES</h3><p>Good design is always in season</p><span class="cta">View Details &rarr;</span>
  </div>
</section>

<h2 class="abs section-title featured-title">FEATURED PRODUCTS</h2>
<div class="abs carousel-arrow" style="left:128px"><svg width="8" height="12" viewBox="0 0 8 12"><path d="M7 1L2 6l5 5" fill="none" stroke="#555" stroke-width="1.5"/></svg></div>
<div class="abs carousel-arrow" style="left:1042px"><svg width="8" height="12" viewBox="0 0 8 12"><path d="M1 1l5 5-5 5" fill="none" stroke="#555" stroke-width="1.5"/></svg></div>
<div class="abs product" style="left:161px"><div class="ph" role="img" aria-label="Modern dining table with black and white chairs" style="background:radial-gradient(ellipse,#8a8a8a,#2a2a2a 55%,#fff 70%)"></div><h4>Luxury Italian Dining Table</h4><a class="btn on">View Details</a></div>
<div class="abs product" style="left:386px"><div class="ph" role="img" aria-label="Dark three door wooden wardrobe" style="background:linear-gradient(90deg,#fff 22%,#4a3424 22%,#5e4330 78%,#fff 78%)"></div><h4>3-Door Wooden Wardrobe</h4><a class="btn">View Details</a></div>
<div class="abs product" style="left:610px"><div class="ph" role="img" aria-label="Black royal dining table with carved chairs" style="background:radial-gradient(ellipse,#555,#111 55%,#fff 70%)"></div><h4>Royal Italian Dining Table</h4><a class="btn">View Details</a></div>
<div class="abs product" style="left:833px"><div class="ph" role="img" aria-label="Cherry wood four door wardrobe with mirrors" style="background:linear-gradient(90deg,#fff 15%,#7a3a1a 15%,#8e4a22 85%,#fff 85%)"></div><h4>4-Door Wooden Wardrobe</h4><a class="btn">View Details</a></div>

<div class="abs news-band" role="img" aria-label="Dim classic dining room interior"></div>
<h2 class="abs section-title news-title">RECENT NEWS</h2>
<article class="abs news" style="left:161px">
  <div class="ph" role="img" aria-label="Baroque antique style dining table in ornate room" style="background:linear-gradient(135deg,#3a2c20,#7a6048 50%,#2a2018)"></div>
  <div class="date"><b>14</b><i>DEC</i></div>
  <h4>Baroque Antique Style Italian Dining Table, 100% Solid Wood Italy Style Luxury Dining Table</h4>
  <p>Lorem ipsum dolor sit amet, consectetuer adipiscing elit, sed diam nonummy nibh euismod tincidunt ut laoreet dolore magna aliquam erat volutpat.</p>
  <a class="more">Read More <svg width="18" height="8" viewBox="0 0 18 8"><path d="M0 4h16M13 1l3 3-3 3" fill="none" stroke="#2b2b2b" stroke-width="1.3"/></svg></a>
</article>
<article class="abs news" style="left:462px">
  <div class="ph" role="img" aria-label="Cream antique style wooden wardrobe in a bedroom" style="background:linear-gradient(135deg,#b0602e,#e6d1ae 50%,#9a5228)"></div>
  <div class="date"><b>14</b><i>DEC</i></div>
  <h4>Antique Style Italian Wooden Wardrobe, 100% Solid Wood Italy Style Wooden Wardrobe</h4>
  <p>Lorem ipsum dolor sit amet, consectetuer adipiscing elit, sed diam nonummy nibh euismod tincidunt ut laoreet dolore magna aliquam erat volutpat.</p>
  <a class="more">Read More <svg width="18" height="8" viewBox="0 0 18 8"><path d="M0 4h16M13 1l3 3-3 3" fill="none" stroke="#2b2b2b" stroke-width="1.3"/></svg></a>
</article>
<article class="abs news" style="left:761px">
  <div class="ph" role="img" aria-label="Black lacquer dining table with chairs in a bright room" style="background:linear-gradient(135deg,#9a9a9a,#222 50%,#bdbdbd)"></div>
  <div class="date"><b>14</b><i>DEC</i></div>
  <h4>Baroque Antique Style Italian Dining Table, 100% Solid Wood Italy Style Luxury Dining Table</h4>
  <p>Lorem ipsum dolor sit amet, consectetuer adipiscing elit, sed diam nonummy nibh euismod tincidunt ut laoreet dolore magna aliquam erat volutpat.</p>
  <a class="more">Read More <svg width="18" height="8" viewBox="0 0 18 8"><path d="M0 4h16M13 1l3 3-3 3" fill="none" stroke="#2b2b2b" stroke-width="1.3"/></svg></a>
</article>

<div class="abs feature" style="left:144px">
  <div class="circle" style="background:var(--brown)"><svg width="52" height="34" viewBox="0 0 52 34"><rect x="4" y="6" width="28" height="18" fill="#fff"/><path d="M32 12h10l6 7v5H32z" fill="#fff"/><circle cx="12" cy="27" r="4" fill="#fff" stroke="#5a3a1e" stroke-width="2"/><circle cx="40" cy="27" r="4" fill="#fff" stroke="#5a3a1e" stroke-width="2"/></svg></div>
  <h5 style="color:var(--brown)">Fast Delivery</h5>
  <p>Lorem ipsum dolor sit amet, consectetuer adipiscing elit, sed diam nonummy nibh euismod tincidunt ut laoreet dolore magna aliquam erat volutpat.</p>
</div>
<div class="abs feature" style="left:449px">
  <div class="circle" style="background:#2a2a2a"><svg width="40" height="44" viewBox="0 0 40 44"><rect x="6" y="4" width="28" height="36" fill="none" stroke="#fff" stroke-width="2.5"/><line x1="20" y1="4" x2="20" y2="40" stroke="#fff" stroke-width="2.5"/><rect x="12" y="24" width="16" height="7" fill="#fff"/></svg></div>
  <h5>Verona Furniture Hire &amp; Rental?</h5>
  <p>Lorem ipsum dolor sit amet, consectetuer adipiscing elit, sed diam nonummy nibh euismod tincidunt ut laoreet dolore magna aliquam erat volutpat.</p>
</div>
<div class="abs feature" style="left:769px">
  <div class="circle" style="background:#2a2a2a"><svg width="44" height="44" viewBox="0 0 44 44"><circle cx="12" cy="12" r="5" fill="none" stroke="#fff" stroke-width="2.5"/><circle cx="12" cy="32" r="5" fill="none" stroke="#fff" stroke-width="2.5"/><path d="M16 15l22 20M16 29l22-20" stroke="#fff" stroke-width="2.5"/></svg></div>
  <h5>Get Inspiration, Ideas and Offers</h5>
  <p>Lorem ipsum dolor sit amet, consectetuer adipiscing elit, sed diam nonummy nibh euismod tincidunt ut laoreet dolore magna aliquam erat volutpat.</p>
</div>

<section class="abs newsletter">
  <div class="ph" role="img" aria-label="Two black carved chairs with patterned upholstery"></div>
  <h3>SIGN UP NEWSLETTER</h3>
  <p>Subscribe to our newsletters now and stay up-to-date with new collections, the latest lookbooks and exclusive offers.</p>
  <div class="field">Enter Your Email Address</div>
  <div class="submit">Subsribe!</div>
</section>

<footer>
  <div class="abs footer" role="img" aria-label="Dark showroom interior"></div>
  <div class="abs footer-brand"><div class="dot"></div><span>VERONA<br>HOME FURNISHINGS</span></div>
  <nav class="abs footer-nav"><a>Home</a><a>Italian Dining Tables</a><a>Wooden Wardrobes</a><a>Product Category</a><a>About</a><a>Faq's</a><a>Contact</a></nav>
  <div class="abs footer-contact" style="left:265px"><div class="ring"><svg width="14" height="18" viewBox="0 0 14 18"><path d="M7 1a6 6 0 0 0-6 6c0 4 6 10 6 10s6-6 6-10a6 6 0 0 0-6-6z" fill="#fff"/><circle cx="7" cy="7" r="2" fill="#111"/></svg></div><div>Verona Home Furnishings<br>210 Harbor Ln - FL 33100</div></div>
  <div class="abs footer-contact" style="left:528px"><div class="ring"><svg width="16" height="16" viewBox="0 0 14 14"><path d="M3 1l2.5 3-1.5 1.5c1 2 2.5 3.5 4.5 4.5L10 8.5 13 11l-1.5 2C6 13 1 8 1 2.5z" fill="#fff"/></svg></div><div>Phone:<br>555-018-2040</div></div>
  <div class="abs footer-contact" style="left:702px"><div class="ring"><svg width="16" height="16" viewBox="0 0 14 14"><path d="M1 6l12-5-5 12-2-5z" fill="#fff"/></svg></div><div>Email:<br>hello@veronahome.example</div></div>
  <div class="abs footer-links">FAQ's<span>|</span>Privacy policy<span>|</span>Terms of use</div>
  <div class="abs footer-bar"></div>
  <div class="abs copyright">Copyright © 2017 Verona Home Furnishings. | All Rights Reserved.</div>
  <div class="abs socials"><i></i><i></i><i style="background:#3a9ad9"></i><i style="background:#c9433a"></i></div>
</footer>

</body>
</html>
```